I already have a logo created by Quillory Makers that I'm very happy with. I need to spruce up my business card now. Its a double sided card with not much info on it, I like to keep it simple.
Front of card: name, phone # email address, web address. Tag Line "Outsourced Technology Solutions", under that it says Business Voice Services & Electronic Protection.
Rear of Card: Content written inside a "cloud" saying "Cloud Solutions" "Cloud Integrity"

Target Market(s)

Business to Business

Industry/Entity Type

Business

Contact Information for Business Card

We are in the technology field. Providing Telephone systems (hardware), SIP Trunks (dial tone/local/long distance/telephone #'s), LAN (Local Area Network)infrastructure cabling, Data Center solutions and Security Applications (Camera systems, Access Control systems,

Requirements
Must have
• Must have brevity
Should not have
• Clutter and/or too much information

```html
<!DOCTYPE html>
<html lang="en">
<head>
<meta charset="utf-8">
<title>Meridian Linkworks – Business Cards</title>
<link rel="stylesheet" href="https://fonts.googleapis.com/css2?family=Open+Sans:wght@300;400;600;700&display=swap">
<style>
  :root {
    --backdrop: #2a2c30;
    --card-white: #ffffff;
    --brand-blue: #1f4690;
    --brand-navy: #1c3a7c;
    --tag-grey: #8a8d93;
    --panel-text: #ffffff;
    --panel-soft: #d5def0;
    --edge-shadow: rgba(0, 0, 0, 0.45);
  }
  * { box-sizing: border-box; margin: 0; padding: 0; }
  html, body { width: 1200px; height: 900px; overflow: hidden; }
  body {
    background: var(--backdrop);
    font-family: "Open Sans", Arial, sans-serif;
    position: relative;
  }
  .card {
    position: absolute;
    width: 540px;
    height: 308px;
    border-radius: 26px;
    background: var(--card-white);
    overflow: hidden;
    box-shadow: 0 14px 30px var(--edge-shadow);
  }
  .card--front { left: 60px; top: 140px; display: flex; }
  .card--back {
    left: 600px; top: 452px;
    display: flex; flex-direction: column;
    align-items: center; justify-content: center; gap: 18px;
  }

  .contact-panel {
    width: 42%;
    height: 100%;
    background: var(--brand-blue);
    color: var(--panel-text);
    padding: 34px 20px 0 28px;
  }
  .contact-panel__name {
    font-weight: 700;
    font-size: 20px;
    letter-spacing: 0.5px;
    text-transform: uppercase;
  }
  .contact-panel__role {
    font-size: 12px;
    color: var(--panel-soft);
    margin-top: 2px;
  }
  .contact-list { list-style: none; margin-top: 36px; }
  .contact-list li {
    display: flex;
    font-size: 12.5px;
    line-height: 1.5;
    margin-bottom: 6px;
  }
  .contact-list__label {
    width: 26px;
    flex: none;
    font-size: 9px;
    color: var(--panel-soft);
    padding-top: 3px;
  }

  .brand-block {
    flex: 1;
    display: flex;
    align-items: center;
    justify-content: center;
    padding: 0 20px;
  }
  .brand {
    display: flex;
    flex-direction: column;
    align-items: flex-start;
  }
  .brand__row { display: flex; align-items: center; gap: 10px; }
  .brand__mark {
    width: 22px; height: 22px;
    background: var(--brand-navy);
    flex: none;
  }
  .brand__name {
    font-weight: 700;
    color: var(--brand-navy);
    font-size: 21px;
    line-height: 1.05;
  }
  .brand__rule {
    width: 100%;
    height: 1px;
    background: var(--tag-grey);
    margin: 7px 0 5px;
  }
  .brand__tagline {
    font-weight: 300;
    color: var(--tag-grey);
    font-size: 13px;
    letter-spacing: 0.2px;
  }
  .brand__services {
    font-weight: 400;
    color: var(--brand-navy);
    font-size: 9.5px;
    margin-top: 4px;
    white-space: nowrap;
  }
  .card--back .brand__name { font-size: 24px; }
  .card--back .brand__mark { width: 24px; height: 24px; }
  .card--back .brand__tagline { font-size: 15px; }

  .cloud {
    position: relative;
    width: 240px;
    height: 112px;
  }
  .cloud__shape { position: absolute; inset: 0; }
  .cloud__text {
    position: absolute;
    left: 0; right: 0; top: 48px;
    text-align: center;
    color: var(--brand-navy);
    font-weight: 600;
    font-size: 14px;
    line-height: 1.35;
  }
</style>
</head>
<body>
  <section class="card card--front" aria-label="Business card front">
    <div class="contact-panel">
      <h1 class="contact-panel__name">Adrian Vell</h1>
      <p class="contact-panel__role">Software Engineer</p>
      <ul class="contact-list">
        <li><span class="contact-list__label">(P)</span>+000 55501 4287</li>
        <li><span class="contact-list__label">(E)</span>adrian@meridianlink.net</li>
        <li><span class="contact-list__label">(W)</span>meridianlink.net</li>
        <li><span class="contact-list__label">(A)</span>18 Harbour Lane<br>Portvale, 5521</li>
      </ul>
    </div>
    <div class="brand-block">
      <div class="brand">
        <div class="brand__row">
          <span class="brand__mark"></span>
          <span class="brand__name">Meridian<br>Linkworks, LLC</span>
        </div>
        <span class="brand__rule"></span>
        <span class="brand__tagline">Outsourced Technology Solutions</span>
        <span class="brand__services">Business Voice Services &amp; Electronic Protection</span>
      </div>
    </div>
  </section>

  <section class="card card--back" aria-label="Business card back">
    <div class="brand">
      <div class="brand__row">
        <span class="brand__mark"></span>
        <span class="brand__name">Meridian<br>Linkworks, LLC</span>
      </div>
      <span class="brand__rule"></span>
      <span class="brand__tagline">Outsourced Technology Solutions</span>
    </div>
    <div class="cloud">
      <svg class="cloud__shape" viewBox="0 0 240 112" aria-hidden="true">
        <path d="M46 104 H196 A30 30 0 0 0 202 45 A42 42 0 0 0 124 24 A36 36 0 0 0 62 42 A31 31 0 0 0 46 104 Z"
              fill="none" stroke="#1c3a7c" stroke-width="2.5" stroke-linejoin="round"/>
      </svg>
      <p class="cloud__text">Cloud Solutions<br>Cloud Integrity</p>
    </div>
  </section>
</body>
</html>
```